R&T Architects - business card and stationary

Aloha,

We have a simple text logo, we need it incorporated into a business card and also stationary design (letterhead) if possible.

Please check out our website, rtamaui-studio.example for a little more about us. The logo we would like to use is in the upper left corner of the website. It is a simple colored logo based on the Klavica font. We are open to new logo's as well, but we want simple.

Thanks

```html
<!DOCTYPE html>
<html lang="en">
<head>
<meta charset="utf-8">
<title>R&amp;T Architects – Business Card</title>
<link rel="stylesheet" href="https://fonts.googleapis.com/css2?family=PT+Sans+Narrow:wght@400;700&display=swap">
<style>
  :root {
    --backdrop: #e6f0e6;
    --paper: #ffffff;
    --stone: #b1b092;
    --olive: #575a1c;
    --leaf: #7fd21c;
    --shadow: rgba(40, 45, 35, 0.45);
  }
  * { margin: 0; padding: 0; box-sizing: border-box; }
  html, body {
    width: 1200px;
    height: 901px;
    overflow: hidden;
    background: var(--backdrop);
    font-family: "PT Sans Narrow", "Arial Narrow", sans-serif;
  }
  .canvas { position: relative; width: 1200px; height: 901px; }

  .card {
    position: absolute;
    width: 608px;
    height: 347px;
    box-shadow: 9px 12px 14px var(--shadow);
    overflow: hidden;
  }

  /* Front card */
  .card--front { left: 71px; top: 68px; background: var(--paper); }
  .card__name {
    height: 105px;
    display: flex;
    align-items: center;
    justify-content: center;
    color: var(--olive);
    font-weight: 700;
    font-size: 37px;
    letter-spacing: 0.3px;
  }
  .card__contact {
    height: 138px;
    background: var(--stone);
    display: flex;
    flex-direction: column;
    justify-content: center;
    align-items: center;
    gap: 5px;
    font-weight: 700;
    font-size: 20px;
    line-height: 26px;
    color: var(--paper);
  }
  .card__label { color: var(--olive); }
  .card__brand {
    height: 104px;
    display: flex;
    align-items: center;
    justify-content: center;
  }

  .wordmark {
    font-weight: 700;
    text-transform: uppercase;
    color: var(--leaf);
    letter-spacing: 2px;
    line-height: 1;
  }
  .wordmark--small { font-size: 60px; }
  .wordmark--large { font-size: 76px; letter-spacing: 3px; }

  /* Back card */
  .card--back { left: 519px; top: 484px; background: var(--stone); }
  .card__strip {
    position: absolute;
    left: 0;
    top: 106px;
    width: 100%;
    height: 138px;
    background: var(--paper);
    display: flex;
    flex-direction: column;
    align-items: center;
    justify-content: center;
    gap: 6px;
  }
  .card__services {
    color: var(--olive);
    font-weight: 700;
    font-size: 18px;
    letter-spacing: 0.6px;
  }
</style>
</head>
<body>
<main class="canvas">
  <section class="card card--front" aria-label="Business card front">
    <h1 class="card__name">Kai Lomond</h1>
    <div class="card__contact">
      <p><span class="card__label">tel</span> +1808 555 0142</p>
      <p><span class="card__label">email</span> kai@rtamaui-studio.example</p>
      <p><span class="card__label">add</span> 48-210 Makana Road, Waimea, Hawaii 96799</p>
    </div>
    <div class="card__brand">
      <span class="wordmark wordmark--small">R&amp;T Architects</span>
    </div>
  </section>

  <section class="card card--back" aria-label="Business card back">
    <div class="card__strip">
      <span class="wordmark wordmark--large">R&amp;T Architects</span>
      <p class="card__services">residential | commercial | structural | LEED | interior | master plan</p>
    </div>
  </section>
</main>
</body>
</html>
```